Torvane Facilities Business Card Design

We would now like to design business cards with the new Torvane Facilities logo

Target Market(s)

Professional

Industry/Entity Type

Professional services

Contact Information for Business Card

Employee name, title, phone number, email address, corporate office address and logo.

Font styles to use
Sans Serif

Colors
0054AA
0677BA
7BADD7
CADEEF
E8F1F8

Requirements
Must have
• My logo
Should not have
• any other pictures or images besides my logo

```html
<!DOCTYPE html>
<html lang="en">
<head>
<meta charset="utf-8">
<title>Torvane Facilities — Business Card</title>
<link href="https://fonts.googleapis.com/css2?family=Montserrat:wght@400;500;600&family=Oswald:wght@600&display=swap" rel="stylesheet">
<style>
  :root {
    --backdrop: #1b1b1c;
    --card: #262627;
    --card-edge: #2b2b2c;
    --accent: #2f7fd0;
    --logo-ink: #d9d9da;
    --text: #f2f2f2;
  }
  * { box-sizing: border-box; margin: 0; padding: 0; }
  html, body { width: 1200px; height: 900px; overflow: hidden; }
  body {
    background: var(--backdrop);
    font-family: "Montserrat", sans-serif;
    position: relative;
  }
  .card {
    position: absolute;
    left: 270px;
    width: 660px;
    height: 377px;
    background: linear-gradient(135deg, var(--card) 0%, var(--card-edge) 60%, #303031 100%);
    border-bottom: 6px solid var(--accent);
    box-shadow: 0 18px 40px rgba(0,0,0,0.55);
  }
  .card--front { top: 53px; }
  .card--back { top: 470px; }

  .brand {
    position: absolute;
    inset: 0 0 6px 0;
    display: flex;
    align-items: center;
    justify-content: center;
    gap: 16px;
  }
  .brand__square {
    width: 26px;
    height: 26px;
    background: var(--logo-ink);
  }
  .brand__name {
    font-family: "Montserrat", sans-serif;
    font-weight: 600;
    font-size: 34px;
    letter-spacing: 0.04em;
    color: var(--logo-ink);
  }

  .identity {
    position: absolute;
    right: 330px;
    top: 142px;
    text-align: right;
  }
  .identity__name {
    font-family: "Oswald", sans-serif;
    font-weight: 600;
    font-size: 44px;
    line-height: 1;
    color: var(--accent);
    text-transform: uppercase;
    letter-spacing: 0.01em;
  }
  .identity__title {
    margin-top: 8px;
    font-size: 17px;
    font-weight: 500;
    color: var(--text);
  }
  .divider {
    position: absolute;
    left: 352px;
    top: 134px;
    width: 2px;
    height: 98px;
    background: var(--accent);
  }
  .contact {
    position: absolute;
    left: 376px;
    top: 138px;
    list-style: none;
    color: var(--text);
    font-size: 17px;
    font-weight: 500;
    line-height: 1.3;
  }
  .contact__item { display: flex; align-items: center; gap: 10px; }
  .contact__item svg { width: 14px; height: 14px; flex: none; }
  .contact__address { margin-bottom: 2px; }
</style>
</head>
<body>
  <section class="card card--front" aria-label="Card front">
    <div class="brand">
      <span class="brand__square" aria-hidden="true"></span>
      <span class="brand__name">Torvane Facilities</span>
    </div>
  </section>

  <section class="card card--back" aria-label="Card back">
    <div class="identity">
      <h1 class="identity__name">Marcus Hale</h1>
      <p class="identity__title">Director</p>
    </div>
    <span class="divider" aria-hidden="true"></span>
    <ul class="contact">
      <li class="contact__address">118 Cedar Bend Road<br>Salem, OR 97301</li>
      <li class="contact__item">
        <svg viewBox="0 0 24 24" aria-hidden="true"><path fill="#2f7fd0" d="M6.6 10.8a15.1 15.1 0 0 0 6.6 6.6l2.2-2.2c.3-.3.7-.4 1-.2 1.1.4 2.3.6 3.6.6.6 0 1 .4 1 1V20c0 .6-.4 1-1 1C10.6 21 3 13.4 3 4c0-.6.4-1 1-1h3.5c.6 0 1 .4 1 1 0 1.3.2 2.5.6 3.6.1.3 0 .7-.2 1L6.6 10.8z"/></svg>
        (555) 214-0387
      </li>
      <li class="contact__item">
        <svg viewBox="0 0 24 24" aria-hidden="true"><rect x="2.5" y="5" width="19" height="14" rx="1.5" fill="none" stroke="#2f7fd0" stroke-width="2"/><path d="M3 6l9 7 9-7" fill="none" stroke="#2f7fd0" stroke-width="2"/></svg>
        info@torvanefacilities.com
      </li>
    </ul>
  </section>
</body>
</html>
```